A New and modern Business Card for Tarvish Commerce Partners Ltd

New and modern Logo and Business Card Attached is the current logo/business card designCurrently the business is called "Tarvish & Co." or TCP Ltd for short. This is subject to change.This business specialises in Telecoms and Energy. We work with the major networks (QX, Z7, etc) and also offer Energy Products saving clients money off their energy bills.These are business to business services.The current design incorporates a Pheonix, indicating rebirth, starting something new.We would like to maintain the Phoenix element but a newer modern style.We love colours in the logo 3 max.The aim of this is to be ultra slick and modern. I envisage Tarvish & Co. on one side of the card with long descriptions on the other side.Side 1:TCP Ltd/Logo?Side 2:TCP Ltd/Logo/Graphic?Brogan & Co.Name:Address:Phone:Email:The design is mostly flexible but must incorporate a Phoenix.For example "Tarvish & Co." with a block phoenix behind the text...up to you.

Industry/Entity Type

Telecommunications

Contact Information for Business Card

Tarvish & Co.
Address:
Name:
Phone:
Email:

Logo Text

Tarvish & Co.

Colors
33a6d7
0792cd
acd037
9bcb3c
f78f20
fece3e

Requirements
Must have
• Phoenix
• 3/4 colours max
• Blue representing Technology (wireless)
• Green for Eco Energy
• Orange for Phoenix
• White business card background
Should not have
• phoenix must not all be red/ orange fire, we are a technology service company and the phoenix colours must represent this. Fire is not representative of our company.

```html
<!DOCTYPE html>
<html lang="en">
<head>
<meta charset="utf-8">
<title>Tarvish Commerce Partners Ltd – Business Card</title>
<link rel="stylesheet" href="https://fonts.googleapis.com/css2?family=Montserrat:wght@700&family=Overpass:wght@400;600&display=swap">
<style>
  :root {
    --stage: #e5e5e5;
    --card: #ffffff;
    --blue: #0792cd;
    --green: #9bcb3c;
    --yellow: #fece3e;
    --orange: #f78f20;
    --white: #ffffff;
  }
  * { margin: 0; padding: 0; box-sizing: border-box; }
  html, body {
    width: 1200px;
    height: 1200px;
    overflow: hidden;
    background: var(--stage);
  }
  .card {
    position: absolute;
    left: 224px;
    width: 752px;
    height: 459px;
    background: var(--card);
    box-shadow: 4px 5px 8px rgba(0, 0, 0, 0.35);
  }
  .card--front { top: 74px; }
  .card--back { top: 658px; }
  .card svg { display: block; width: 100%; height: 100%; }
  .holder-name { font-family: "Montserrat", sans-serif; font-weight: 700; fill: var(--blue); }
  .holder-role { font-family: "Montserrat", sans-serif; font-weight: 700; fill: var(--green); }
  .contact-line { font-family: "Overpass", sans-serif; font-weight: 400; fill: var(--blue); }
  .brand-name { font-family: "Overpass", sans-serif; font-weight: 600; }
  .brand-name--light { fill: var(--white); }
  .brand-name--blue { fill: var(--blue); }
  .fill-blue { fill: var(--blue); }
  .fill-green { fill: var(--green); }
  .fill-yellow { fill: var(--yellow); }
  .fill-orange { fill: var(--orange); }
</style>
</head>
<body>

<section class="card card--front" aria-label="Card front with contact details">
  <svg viewBox="0 0 940 574" xmlns="http://www.w3.org/2000/svg">
    <!-- arrow panel -->
    <polygon class="fill-blue" points="320,192 336,192 428,287 336,382 320,382 413,287"/>
    <polygon class="fill-green" points="228,120 248,120 415,287 248,454 228,454 395,287"/>
    <polygon class="fill-blue" points="0,120 205,120 372,287 205,454 0,454"/>
    <text class="brand-name brand-name--light" x="117" y="286" font-size="40">TCP Ltd</text>

    <!-- name block -->
    <text class="holder-name" x="844" y="96" font-size="58" text-anchor="end">YourName</text>
    <text class="holder-role" x="844" y="144" font-size="33" text-anchor="end">Position</text>

    <!-- contact lines -->
    <text class="contact-line" x="844" y="270" font-size="23" text-anchor="end" letter-spacing="0.5">Address</text>
    <text class="contact-line" x="844" y="346" font-size="23" text-anchor="end" letter-spacing="0.5">123-xxx-xxxx</text>
    <text class="contact-line" x="844" y="418" font-size="23" text-anchor="end" letter-spacing="0.5">your@email.com</text>

    <!-- pin icon -->
    <g class="fill-blue" transform="translate(880,262)">
      <path d="M0,-13 C-7,-13 -10,-8 -10,-3 C-10,4 0,14 0,14 C0,14 10,4 10,-3 C10,-8 7,-13 0,-13 Z M0,-7 A4,4 0 1 0 0.01,-7 Z" fill-rule="evenodd"/>
    </g>
    <!-- phone icon -->
    <g transform="translate(880,337)">
      <path class="fill-blue" d="M-9,-9 L-4,-10 L-1,-4 L-4,-2 C-3,1 0,4 3,5 L5,2 L11,5 L10,10 C2,11 -10,0 -9,-9 Z"/>
      <path d="M1,-9 A8,8 0 0 1 9,-1 M1,-5 A4,4 0 0 1 5,-1" fill="none" stroke="var(--blue)" stroke-width="2"/>
    </g>
    <!-- mail icon -->
    <g transform="translate(880,409)">
      <rect class="fill-blue" x="-11" y="-8" width="22" height="16"/>
      <path d="M-11,-8 L0,2 L11,-8 M-11,8 L-3,-1 M11,8 L3,-1" fill="none" stroke="var(--white)" stroke-width="1.6"/>
    </g>

    <!-- bottom bands -->
    <polygon class="fill-yellow" points="277,574 340,512 662,512 600,574"/>
    <polygon class="fill-green" points="688,488 940,488 940,543 634,543"/>
    <polygon class="fill-blue" points="520,543 940,543 940,574 487,574"/>
  </svg>
</section>

<section class="card card--back" aria-label="Card back with company name">
  <svg viewBox="0 0 940 574" xmlns="http://www.w3.org/2000/svg">
    <text class="brand-name brand-name--blue" x="470" y="300" font-size="72" text-anchor="middle">TCP Ltd</text>
    <rect class="fill-green" x="0" y="544" width="940" height="30"/>
    <polygon class="fill-orange" points="328,514 610,514 670,574 268,574"/>
  </svg>
</section>

</body>
</html>
```